Facebook & Instagram Ad Design for Chiropractor

I'd like a series of ads developed for our chiropractic office to use on Facebook and Instagram. I've attached the versions we're using today. They need to be updated. The offer content would be generally the same. There are two types of ads we're seeking. One for basic chiropractic services and the other for chiropractic decompression services.

Current ads can be seen in attached and here:
https://lnk.example/8TrQ2zXvPoLkm3A

Learn more about the company at www.bellwingchiropractic.example

Target Market(s)

Potential patients seeking chiropractic care or who are unaware that chiropractic could help them (suffer from back pain, etc.) in the greater Green Bay, WI area.

Industry/Entity Type

Chiropractic

Font styles to use
Sans Serif

Colors
0592cd
3277b5

Requirements
Must have
• Compelling visuals
Comply with text requirements for FB & Insta ads
Should not have
• Clinical images that depict traditional medical care

```html
<!DOCTYPE html>
<html lang="en">
<head>
<meta charset="utf-8">
<title>Chiropractic Service Ads</title>
<link href="https://fonts.googleapis.com/css2?family=Bebas+Neue&family=Poppins:wght@400;600&display=swap" rel="stylesheet">
<style>
  :root {
    --page-bg: #f1f1f3;
    --brand-blue: #3277b5;
    --brand-cyan: #0592cd;
    --deep-blue: #2a6aab;
    --white: #ffffff;
    --skin-light: #e2b9a2;
    --skin-mid: #c98f72;
    --skin-dark: #9c6650;
  }
  * { margin: 0; padding: 0; box-sizing: border-box; }
  html, body { width: 682px; height: 1200px; overflow: hidden; }
  body { background: var(--page-bg); position: relative; font-family: "Poppins", sans-serif; }

  .ad {
    position: absolute;
    left: 18px;
    width: 646px;
    overflow: hidden;
  }
  .ad--one   { top: 18px;  height: 392px; background: linear-gradient(90deg, var(--brand-blue) 0%, var(--brand-blue) 100%); }
  .ad--two   { top: 440px; height: 362px; background: linear-gradient(180deg, var(--brand-cyan) 0%, #1a84c8 100%); }
  .ad--three { top: 826px; height: 356px; background: linear-gradient(90deg, var(--deep-blue) 0%, var(--brand-blue) 100%); }

  .ad__photo { position: absolute; top: 0; left: 0; height: 100%; }
  .ad--one .ad__photo {
    width: 440px;
    background:
      linear-gradient(90deg, rgba(50,119,181,0) 0%, rgba(50,119,181,0) 45%, var(--brand-blue) 100%),
      radial-gradient(ellipse at 35% 55%, var(--skin-light) 0%, var(--skin-mid) 45%, var(--skin-dark) 100%);
  }
  .ad--two .ad__photo,
  .ad--three .ad__photo {
    width: 318px;
    background: radial-gradient(ellipse at 50% 60%, var(--skin-light) 0%, var(--skin-mid) 55%, var(--skin-dark) 100%);
  }

  .ad__copy { position: absolute; color: var(--white); }
  .ad--one .ad__copy   { left: 380px; top: 90px; }
  .ad--two .ad__copy   { left: 352px; top: 86px; }
  .ad--three .ad__copy { left: 352px; top: 82px; }

  .ad__headline {
    font-family: "Bebas Neue", sans-serif;
    font-weight: 400;
    font-size: 58px;
    line-height: 0.92;
    letter-spacing: 0.5px;
  }
  .ad__note { font-size: 12px; margin-top: 26px; }
  .ad__url { font-size: 12.5px; font-weight: 600; margin-top: 6px; }
</style>
</head>
<body>
  <section class="ad ad--one">
    <div class="ad__photo" role="img" aria-label="Chiropractor's hands adjusting a patient's bare upper back and shoulder"></div>
    <div class="ad__copy">
      <h2 class="ad__headline">Need a<br>Chiropractic<br>Service?</h2>
      <p class="ad__note">For More information, Visit:</p>
      <p class="ad__url">www.bellwing-spine-care.example</p>
    </div>
  </section>

  <section class="ad ad--two">
    <div class="ad__photo" role="img" aria-label="Chiropractor's hands pressing on a patient's bare back while holding the shoulder"></div>
    <div class="ad__copy">
      <h2 class="ad__headline">Need a<br>Chiropractic<br>Service?</h2>
      <p class="ad__note">For More information, Visit:</p>
      <p class="ad__url">www.bellwing-spine-care.example</p>
    </div>
  </section>

  <section class="ad ad--three">
    <div class="ad__photo" role="img" aria-label="Chiropractor's hands pressing on a patient's bare back while holding the shoulder"></div>
    <div class="ad__copy">
      <h2 class="ad__headline">Need a<br>Chiropractic<br>Service?</h2>
      <p class="ad__note">For More information, Visit:</p>
      <p class="ad__url">www.bellwing-spine-care.example</p>
    </div>
  </section>
</body>
</html>
```